Bref créative
Business cards and stationery for investment company
Velorin Holdings
Professional
Owen Pellick
P.O. Box YYY
Elmsworth, Westland 84219
owen.pellick@velorin.example
www.velorin.example
Logo only

```html
<!DOCTYPE html>
<html lang="en">
<head>
<meta charset="utf-8">
<title>Velorin Holdings – Business Cards</title>
<link href="https://fonts.googleapis.com/css2?family=Cinzel:wght@600&family=Open+Sans:wght@400;700&display=swap" rel="stylesheet">
<style>
  :root{
    --bg:#2b2b2b;
    --red:#c8141c;
    --red-dark:#8e0a10;
    --red-light:#e2323a;
    --white:#ffffff;
    --paper:#f4f4f4;
    --ink:#4a4a4a;
  }
  html,body{margin:0;padding:0;overflow:hidden;}
  body{width:1200px;height:901px;background:var(--bg);position:relative;font-family:"Open Sans",sans-serif;}
  .card{position:absolute;left:250px;width:700px;height:400px;border-radius:22px;overflow:hidden;box-shadow:0 10px 30px rgba(0,0,0,.45);}
  .card--front{top:30px;background:radial-gradient(ellipse at 35% 30%,var(--red-light),var(--red) 45%,var(--red-dark));}
  .card--back{top:470px;background:linear-gradient(160deg,var(--white),var(--paper));}
  .front-brand{position:absolute;left:0;right:0;top:160px;text-align:center;}
  .front-brand__name{font-family:"Cinzel",serif;font-weight:600;font-size:46px;color:var(--white);letter-spacing:2px;}
  .front-brand__web{margin-top:14px;font-size:16px;color:rgba(255,255,255,.55);letter-spacing:1px;}
  .back-brand{position:absolute;left:44px;top:40px;display:flex;align-items:center;gap:14px;}
  .back-brand__mark{width:30px;height:30px;border-radius:50%;background:var(--red);}
  .back-brand__name{font-family:"Cinzel",serif;font-weight:600;font-size:32px;color:var(--red);letter-spacing:1px;}
  .contact{position:absolute;left:44px;top:110px;font-size:17px;line-height:26px;color:var(--ink);}
  .contact__row{display:flex;align-items:center;gap:10px;}
  .contact__row svg{width:15px;height:15px;flex:none;}
  .contact__address{margin-bottom:6px;}
  .swoosh{position:absolute;left:0;bottom:0;width:700px;height:200px;}
  .holder-name{position:absolute;right:40px;bottom:34px;font-size:30px;font-weight:700;color:var(--white);}
</style>
</head>
<body>
  <section class="card card--front" aria-label="Card front">
    <div class="front-brand">
      <div class="front-brand__name">Velorin Holdings</div>
      <div class="front-brand__web">www.velorin.example</div>
    </div>
  </section>

  <section class="card card--back" aria-label="Card back">
    <div class="back-brand">
      <span class="back-brand__mark"></span>
      <span class="back-brand__name">Velorin Holdings</span>
    </div>
    <div class="contact">
      <div class="contact__address">P.O. Box YYY<br>Elmsworth, Westland 84219</div>
      <div class="contact__row">
        <svg viewBox="0 0 16 16"><path fill="#c8141c" d="M3 1h3l1 4-2 1a9 9 0 0 0 5 5l1-2 4 1v3a2 2 0 0 1-2 2A13 13 0 0 1 1 3a2 2 0 0 1 2-2z"/></svg>
        <span>555-201-0142</span>
      </div>
      <div class="contact__row">
        <svg viewBox="0 0 16 16"><rect x="1" y="3" width="14" height="10" rx="1" fill="none" stroke="#c8141c" stroke-width="1.6"/><path d="M1 4l7 5 7-5" fill="none" stroke="#c8141c" stroke-width="1.6"/></svg>
        <span>owen.pellick@velorin.example</span>
      </div>
      <div class="contact__row">
        <svg viewBox="0 0 16 16"><circle cx="8" cy="8" r="6.5" fill="none" stroke="#c8141c" stroke-width="1.6"/><path d="M1.5 8h13M8 1.5c3 3 3 10 0 13M8 1.5c-3 3-3 10 0 13" fill="none" stroke="#c8141c" stroke-width="1.2"/></svg>
        <span>www.velorin.example</span>
      </div>
    </div>
    <svg class="swoosh" viewBox="0 0 700 200" aria-hidden="true">
      <defs>
        <linearGradient id="bandRed" x1="0" y1="0" x2="1" y2="1">
          <stop offset="0" stop-color="#e2323a"/>
          <stop offset="1" stop-color="#8e0a10"/>
        </linearGradient>
        <linearGradient id="bandGrey" x1="0" y1="0" x2="1" y2="0">
          <stop offset="0" stop-color="#d0d0d0"/>
          <stop offset="1" stop-color="#8a8a8a"/>
        </linearGradient>
      </defs>
      <path d="M0 90 C200 150 450 40 700 30 L700 60 C460 70 220 170 0 120 Z" fill="url(#bandGrey)"/>
      <path d="M0 130 C220 180 460 80 700 66 L700 200 L0 200 Z" fill="url(#bandRed)"/>
    </svg>
    <div class="holder-name">Owen Pellick</div>
  </section>
</body>
</html>
```